Holiday Light Door Hanger

I need a new doorhanger design for our Holiday Light Service. I have attached our last one (which we DO like), but need to have a two-sided design. I also will attach photos that can be used as well as a FAQ about the service.

```html
<!DOCTYPE html>
<html lang="en">
<head>
<meta charset="utf-8">
<title>Holiday Light Door Hanger</title>
<link href="https://fonts.googleapis.com/css2?family=Abril+Fatface&family=Barlow+Condensed:wght@600&family=Oswald:wght@500;600;700&family=Poppins:wght@400;500;600;700;800&display=swap" rel="stylesheet">
<style>
  :root {
    --stage: #e3e4e8;
    --navy: #1c2540;
    --navy-deep: #151c33;
    --red: #e01b1b;
    --green: #4d9b2b;
    --green-bright: #5aae2e;
    --blue: #1a4e9c;
    --white: #ffffff;
    --ink: #222222;
  }
  * { margin: 0; padding: 0; box-sizing: border-box; }
  html, body { width: 1150px; height: 1200px; overflow: hidden; }
  body { background: var(--stage); position: relative; font-family: "Poppins", sans-serif; }

  .hanger {
    position: absolute; top: 117px; width: 386px; height: 965px;
    border-radius: 34px 34px 40px 40px; overflow: hidden; background: var(--navy);
  }
  .hanger--front { left: 139px; }
  .hanger--back { left: 626px; }
  .layer { position: absolute; left: 0; top: 0; }
  .hole { position: absolute; left: 0; top: 0; z-index: 20; }

  .brand-name {
    font-family: "Oswald", sans-serif; font-weight: 600; letter-spacing: 1px;
    display: flex; align-items: center; gap: 6px;
  }
  .brand-name .mark { width: 10px; height: 10px; background: var(--green); display: inline-block; }

  /* front */
  .front-brand { position: absolute; left: 28px; top: 390px; color: var(--white); font-size: 22px; z-index: 5; }
  .front-title {
    position: absolute; left: 26px; top: 442px; z-index: 5;
    font-family: "Oswald", sans-serif; font-weight: 700; font-size: 46px; line-height: 47px; text-transform: uppercase;
  }
  .front-title .t-white { color: var(--white); }
  .front-title .t-red { color: var(--red); }
  .front-title .t-green { color: var(--green-bright); }
  .front-sub { position: absolute; left: 26px; top: 586px; color: var(--white); font-weight: 500; font-size: 17px; z-index: 5; }
  .gallery {
    position: absolute; left: 25px; top: 641px; width: 335px; height: 111px; z-index: 5;
    border: 3px solid #e8ebf0; border-radius: 10px 22px 10px 22px; padding: 3px;
    display: flex; gap: 7px; background: #e8ebf0;
  }
  .gallery .shot { flex: 1; height: 100%; }
  .shot--barn { background: linear-gradient(160deg, #2a3f7a, #6c7fb0 60%, #d5dbe8); border-radius: 0 0 0 14px; }
  .shot--home { background: linear-gradient(170deg, #0f1c3d, #1d3b2a 55%, #a0302a); }
  .shot--office { background: linear-gradient(170deg, #1a2f73, #2a3550 55%, #8a6a3a); border-radius: 0 16px 0 0; }
  .season { position: absolute; left: 0; width: 100%; top: 765px; text-align: center; z-index: 5;
    font-family: "Abril Fatface", serif; color: var(--white); font-size: 26px; letter-spacing: 0.5px; }

  /* footer */
  .footer { position: absolute; left: 0; right: 0; bottom: 0; height: 98px; z-index: 6; }
  .footer-brand { position: absolute; left: 25px; top: 6px; color: var(--blue); font-size: 17px; }
  .footer-note { position: absolute; left: 25px; top: 38px; width: 150px; font-size: 6.4px; line-height: 8px; color: var(--ink); }
  .footer-note b { font-weight: 700; }
  .contact { position: absolute; right: 24px; top: 12px; }
  .contact-row { display: flex; align-items: flex-end; gap: 6px; }
  .contact-label { font-size: 8px; font-weight: 600; color: var(--green); letter-spacing: 0.3px; }
  .contact-phone { font-size: 18px; font-weight: 700; color: var(--blue); line-height: 20px; letter-spacing: 0.5px; }
  .contact-email { font-size: 11px; font-weight: 600; color: var(--blue); margin-top: 5px; }
  .contact-email span { color: var(--green); }

  /* back */
  .back-title {
    position: absolute; left: 28px; top: 187px; z-index: 5;
    font-family: "Oswald", sans-serif; font-weight: 600; font-size: 32px; line-height: 36px;
    color: var(--white); text-transform: uppercase;
  }
  .back-title .t-red { color: var(--red); }
  .back-title .t-green { color: var(--green-bright); }
  .back-copy { position: absolute; left: 28px; top: 376px; width: 314px; z-index: 5;
    color: var(--white); font-size: 12.3px; line-height: 15.6px; }
  .price { position: absolute; left: 27px; z-index: 5; color: var(--white); width: 148px; }
  .price-label { font-family: "Barlow Condensed", sans-serif; font-weight: 600; font-size: 16px; line-height: 18px; text-transform: uppercase; }
  .price-value { font-weight: 800; font-size: 35px; line-height: 40px; }
  .price-rule { height: 1px; background: rgba(255,255,255,0.55); margin-top: 2px; }
  .price--average { top: 652px; }
  .price--minimum { top: 770px; }
</style>
</head>
<body>

<!-- Front side -->
<section class="hanger hanger--front">
  <svg class="layer" width="386" height="965" viewBox="0 0 386 965">
    <defs>
      <linearGradient id="houseGlow" x1="0" y1="0" x2="1" y2="1">
        <stop offset="0" stop-color="#6e5a6e"/>
        <stop offset="0.4" stop-color="#5a4f8e"/>
        <stop offset="0.75" stop-color="#3c4a2e"/>
        <stop offset="1" stop-color="#2a3a22"/>
      </linearGradient>
    </defs>
    <rect width="386" height="540" fill="url(#houseGlow)" role="img" aria-label="Photo of a house lit with blue and white holiday lights and lit trees"/>
    <polygon points="0,245 386,418 386,610 0,610" fill="#ffffff"/>
    <polygon points="0,268 38,290 0,372" fill="var(--green)"/>
    <polygon points="386,392 386,480 348,458" fill="var(--green)"/>
    <polygon points="0,378 48,296 386,500 386,965 0,965" fill="var(--navy)"/>
    <polygon points="386,484 386,500 360,484" fill="#ffffff"/>
    <rect x="0" y="805" width="386" height="70" fill="#2a3b4a" opacity="0.55" role="img" aria-label="Illustration of snowy pine trees and a small red cottage"/>
    <path d="M0 868 Q100 852 200 864 T386 860 V965 H0 Z" fill="#ffffff"/>
  </svg>

  <div class="front-brand brand-name"><i class="mark"></i>KEYSTONE YARD</div>
  <h1 class="front-title">
    <span class="t-white">Christmas</span><br>
    <span class="t-red">Light</span><br>
    <span class="t-green">Decorators</span>
  </h1>
  <p class="front-sub">Let Us Handle Your Lights!</p>
  <div class="gallery">
    <div class="shot shot--barn" role="img" aria-label="Barn outlined in white lights at night"></div>
    <div class="shot shot--home" role="img" aria-label="Home with red and green lit trees at night"></div>
    <div class="shot shot--office" role="img" aria-label="Commercial building with roofline lights at dusk"></div>
  </div>
  <p class="season">Enjoy The Season!</p>

  <footer class="footer">
    <div class="footer-brand brand-name">KEYSTONE YARD</div>
    <p class="footer-note">Let Us Know About The Issue You Are Having And We Will Have Someone Out Within <b>48 Hours</b> To Repair The Lights.</p>
    <div class="contact">
      <div class="contact-row">
        <svg width="22" height="22" viewBox="0 0 24 24"><path d="M6.6 10.8c1.4 2.8 3.8 5.1 6.6 6.6l2.2-2.2c.3-.3.7-.4 1-.2 1.1.4 2.3.6 3.6.6.6 0 1 .4 1 1V20c0 .6-.4 1-1 1C10.6 21 3 13.4 3 4c0-.6.4-1 1-1h3.5c.6 0 1 .4 1 1 0 1.3.2 2.5.6 3.6.1.3 0 .7-.2 1z" fill="var(--green)"/></svg>
        <div>
          <div class="contact-label">CALL US TODAY :</div>
          <div class="contact-phone">(555) 214-0396</div>
        </div>
      </div>
      <div class="contact-email"><span>Email:</span> hello@keystoneyard.com</div>
    </div>
  </footer>

  <svg class="hole" width="386" height="200" viewBox="0 0 386 200">
    <circle cx="193" cy="118" r="71" fill="var(--stage)"/>
    <rect x="0" y="103" width="193" height="34" fill="var(--stage)"/>
  </svg>
</section>

<!-- Back side -->
<section class="hanger hanger--back">
  <svg class="layer" width="386" height="965" viewBox="0 0 386 965">
    <defs>
      <linearGradient id="nightHouse" x1="0" y1="0" x2="1" y2="1">
        <stop offset="0" stop-color="#28324f"/>
        <stop offset="0.6" stop-color="#1f2843"/>
        <stop offset="1" stop-color="#19213a"/>
      </linearGradient>
      <linearGradient id="installer" x1="0" y1="0" x2="1" y2="1">
        <stop offset="0" stop-color="#b7c2cf"/>
        <stop offset="0.5" stop-color="#4c5a3a"/>
        <stop offset="1" stop-color="#8a4a3a"/>
      </linearGradient>
    </defs>
    <rect width="386" height="965" fill="url(#nightHouse)" role="img" aria-label="Faded night photo of a house with holiday lights"/>
    <rect x="250" y="0" width="136" height="190" fill="#2d4a33" opacity="0.35" role="img" aria-label="Pine branches with striped red ornaments"/>
    <polygon points="0,456 386,682 386,706 46,508 0,585" fill="#ffffff"/>
    <polygon points="0,469 38,491 0,570" fill="var(--red)"/>
    <polygon points="0,582 46,510 386,708 386,965 0,965" fill="var(--green-bright)"/>
    <circle cx="292" cy="614" r="124" fill="none" stroke="var(--blue)" stroke-width="7"/>
    <circle cx="292" cy="614" r="113" fill="#ffffff"/>
    <circle cx="292" cy="614" r="108" fill="url(#installer)" role="img" aria-label="Photo of a technician on a ladder hanging roofline lights"/>
    <rect x="172" y="760" width="214" height="130" fill="#c0392b" opacity="0.45" role="img" aria-label="Illustration of wrapped gifts and red ornaments"/>
    <path d="M0 872 Q120 860 230 876 T386 872 V965 H0 Z" fill="#ffffff"/>
  </svg>

  <h2 class="back-title">
    We Will<br>
    <span class="t-red">Furnish Custom</span><br>
    <span class="t-red">Cut</span> <span class="t-green">Commercial Lights</span><br>
    In Your Choice<br>
    Of Color Or Pattern
  </h2>
  <p class="back-copy">As well as all needed timers, extension cords or other accessories. Throughout the year we will return for any service issue to make sure your lights are rocking all season! Once the season is over, we will remove all lights, and safely store all items for the following season.</p>

  <div class="price price--average">
    <div class="price-label">The Average<br>Cost For Roofline<br>Installation Is</div>
    <div class="price-value">$1200</div>
    <div class="price-rule"></div>
  </div>
  <div class="price price--minimum">
    <div class="price-label">With A<br>Minimum Charge Of</div>
    <div class="price-value">$500</div>
    <div class="price-rule"></div>
  </div>

  <footer class="footer">
    <div class="footer-brand brand-name">KEYSTONE YARD</div>
    <p class="footer-note">Let Us Know About The Issue You Are Having And We Will Have Someone Out Within <b>48 Hours</b> To Repair The Lights.</p>
    <div class="contact" style="top:19px">
      <div class="contact-row">
        <svg width="22" height="22" viewBox="0 0 24 24"><path d="M6.6 10.8c1.4 2.8 3.8 5.1 6.6 6.6l2.2-2.2c.3-.3.7-.4 1-.2 1.1.4 2.3.6 3.6.6.6 0 1 .4 1 1V20c0 .6-.4 1-1 1C10.6 21 3 13.4 3 4c0-.6.4-1 1-1h3.5c.6 0 1 .4 1 1 0 1.3.2 2.5.6 3.6.1.3 0 .7-.2 1z" fill="var(--green)"/></svg>
        <div>
          <div class="contact-label">CALL US TODAY :</div>
          <div class="contact-phone">(555) 214-0396</div>
        </div>
      </div>
      <div class="contact-email"><span>Email:</span> hello@keystoneyard.com</div>
    </div>
  </footer>

  <svg class="hole" width="386" height="200" viewBox="0 0 386 200">
    <circle cx="193" cy="118" r="71" fill="var(--stage)"/>
    <rect x="0" y="103" width="193" height="34" fill="var(--stage)"/>
  </svg>
</section>

</body>
</html>
```